Flyer-Design für renomiertes Kosmetikstudio
Zielgruppe
Renomiertes Kosmetikstudio sucht hochwertiges Design für neue Flyer.
Zielgruppe Männer + Frauen die auf ihr Äußeres viel Wert legen.
Aufgabenstellung
Geradliniges Desgin unter Berücksichtigung von ganzheitlichen Farben (chakren). Edel.
Wir hätten gerne ein Angebot für Männer als auch für Frauen. Evtl. Aufteilung in 2 getrennte Flyer oder Flyer auf einer Seite Männer und umgedreht auf der anderen Seite für Frauen.?
Behandlungsbereiche die aufgenommen werden müssten:
Frauen
- Wimpernverlängerung
- Wimpernlifting
- Kosmetikbehandlung (Fresh Start - Encore Konzept) ausführlicher text dazu
zzgl. möglichen Bausteinen
- Fußpflege
- Nageldesign
- Enthaarung mit Zuckerpaste
- Massagen
Männer:
- Kosmetikbehandlung
- Maniküre
-- Massage
- Enthaarung
Für die Kosmetik hätte ich gerne jeweils 1 Seite komplett um hier mehr Infos rein zu packen zur FRESH START Behandlung.
Platz für Preise der Behandlungen und bausteine.
Gewünscht Din Lang Format, gerne aber auch offen für neue Ideen.

```html
<!DOCTYPE html>
<html lang="de">
<head>
<meta charset="utf-8">
<title>lumara – Preisliste und Angebote für Männer</title>
<link rel="stylesheet" href="https://fonts.googleapis.com/css2?family=Fira+Sans:wght@300;400;500;600;700&display=swap">
<style>
:root{
  --pink:#e874ab;
  --pink-soft:#ee93bf;
  --magenta:#d4367f;
  --magenta-dark:#c42f77;
  --grey-wave:#5a5a5a;
  --grey-line:#8a8a8a;
  --row:#ececec;
  --text:#4a4a4a;
  --paper:#ffffff;
  --backdrop:#e9e9e9;
}
*{box-sizing:border-box;margin:0;padding:0}
html,body{width:1200px;height:2730px;overflow:hidden}
body{background:var(--backdrop);font-family:"Fira Sans",Arial,sans-serif;color:var(--text);position:relative}

.sheet{position:absolute;background:var(--paper);overflow:hidden;box-shadow:0 6px 24px rgba(0,0,0,.12)}
.trifold{left:100px;width:1000px;height:707px}
.trifold-outside{top:50px}
.trifold-inside{top:830px}
.panel{position:absolute;top:0;width:333.33px;height:100%;overflow:hidden}
.panel-1{left:0}.panel-2{left:333.33px}.panel-3{left:666.66px}
.panel+.panel{border-left:1px solid #f0f0f0}

.abs{position:absolute}
.photo{position:absolute;display:block}
.wave{position:absolute;left:0;width:100%;display:block}
.pink-fill{position:absolute;left:0;width:100%;background:var(--pink)}

.brand{display:flex;align-items:center;justify-content:center;gap:.3em;font-family:"Fira Sans",Arial,sans-serif;font-weight:600;color:var(--magenta);letter-spacing:0;line-height:1}
.brand-dot{display:inline-block;width:.42em;height:.42em;border-radius:50%;background:var(--magenta);flex:none}

.section-title{color:var(--magenta);font-weight:600;line-height:1.1}
.top-rule{position:absolute;left:0;top:0;width:100%;height:10px;background:var(--pink)}
.intro{font-weight:300;line-height:1.35}

.price-box{position:absolute;border:2px solid var(--grey-line);border-radius:6px;padding:14px 6px 6px}
.price-label{position:absolute;left:50%;transform:translateX(-50%);top:-10px;background:var(--pink);color:#fff;border-radius:5px;padding:1px 12px;white-space:nowrap;font-weight:400}
.row{display:grid;align-items:center;padding:0 6px;font-weight:500;white-space:nowrap}
.row>span:first-child{overflow:hidden;text-overflow:ellipsis}
.row:nth-child(odd){background:var(--row)}
.row .dur,.row .cost{display:flex;align-items:center;gap:4px;border-left:1px solid #999;padding-left:6px;justify-content:flex-start}
.row .cost{justify-content:flex-end}
.ico-time,.ico-euro{display:inline-block;border:1.2px solid var(--pink);border-radius:50%;position:relative;flex:none;font-style:normal;color:var(--pink);text-align:center;font-weight:600}
.ico-time::before{content:"";position:absolute;left:45%;top:18%;width:1.2px;height:35%;background:var(--pink)}
.ico-time::after{content:"";position:absolute;left:45%;top:50%;width:30%;height:1.2px;background:var(--pink)}

.price-box.is-large{font-size:9.5px}
.is-large .price-label{font-size:13px;top:-11px}
.is-large .row{grid-template-columns:1fr 64px 60px;height:21px;font-weight:500}
.is-large .ico-time,.is-large .ico-euro{width:10px;height:10px;font-size:7px;line-height:8px}

.price-box.is-small{font-size:6px;padding:10px 4px 4px;border-width:1.5px}
.is-small .price-label{font-size:7px;top:-7px;padding:0 8px}
.is-small .row{grid-template-columns:1fr 44px 40px;height:10.5px;padding:0 3px}
.is-small .row .dur,.is-small .row .cost{gap:2px;padding-left:3px}
.is-small .ico-time,.is-small .ico-euro{width:6px;height:6px;font-size:4px;line-height:4px;border-width:.8px}

.phone-card{position:absolute;background:var(--magenta);border:2px solid #fff;outline:2px solid var(--magenta);border-radius:14px 14px 0 14px;color:#fff;text-align:center;display:flex;flex-direction:column;align-items:center;justify-content:center}
.phone-card .label{letter-spacing:.18em;font-weight:400}
.phone-card .number{font-weight:400;line-height:1.05}

.url-pill{position:absolute;background:var(--magenta-dark);color:#fff;border-radius:8px;text-align:center;font-weight:400}
.contact-title{color:#fff;font-weight:500;text-decoration:underline;text-underline-offset:3px}
.contact-line{color:#fff;font-weight:300;display:flex;gap:6px;align-items:flex-start}
.contact-line svg{flex:none;margin-top:2px}

.headline-white{color:#fff;text-align:center;font-weight:400;letter-spacing:.08em}
.subline{color:#fff;display:flex;align-items:center;justify-content:center;gap:8px;font-weight:300}
.subline::before,.subline::after{content:"";width:54px;height:1px;background:#fff}

.flyer{top:1658px;width:398px;height:797px;box-shadow:none}
.flyer-front{left:148px}
.flyer-back{left:603px}

.hours{display:grid;grid-template-columns:52px 1fr;font-size:6.5px;font-weight:300;line-height:1.45}
.body-copy{font-size:6.3px;line-height:1.4;font-weight:300}
.pill-sub{position:absolute;background:var(--pink);color:#fff;border-radius:4px;font-size:7.5px;padding:1px 10px;font-style:italic;text-align:center}
</style>
</head>
<body>

<section class="sheet trifold trifold-outside" aria-label="Preisliste Außenseite">

  <div class="panel panel-1">
    <div class="top-rule" style="height:4px;width:60%"></div>
    <h2 class="section-title abs" style="left:16px;top:26px;font-size:13px">Fußpflege</h2>
    <p class="intro abs" style="left:16px;top:44px;width:300px;font-size:6px">Klassische Fußpflege mit Fußbad auf Wunsch gerne auch mit Lack oder Dauerformen Nagellack. Zuschläge – Fußmassage, Fußmaske etc.</p>
    <div class="price-box is-small" style="left:16px;top:72px;width:300px">
      <span class="price-label">Fußpflege</span>
      <div class="row"><span>Klassische Fußpflege inkl. Fußbad</span><span class="dur"><i class="ico-time"></i>50 min.</span><span class="cost"><i class="ico-euro">€</i>38,00</span></div>
      <div class="row"><span>Fußpflege mit dauerhaftem Lack</span><span class="dur"><i class="ico-time"></i>75 min.</span><span class="cost"><i class="ico-euro">€</i>53,00</span></div>
      <div class="row"><span>Zuschlag: Klarlack</span><span class="dur"><i class="ico-time"></i>5 min.</span><span class="cost"><i class="ico-euro">€</i>5,00</span></div>
      <div class="row"><span>Zuschlag: Farblack</span><span class="dur"><i class="ico-time"></i>10 min.</span><span class="cost"><i class="ico-euro">€</i>8,00</span></div>
      <div class="row"><span>Fußpeeling</span><span class="dur"><i class="ico-time"></i>15 min.</span><span class="cost"><i class="ico-euro">€</i>9,00</span></div>
      <div class="row"><span>Kleine Fußmassage</span><span class="dur"><i class="ico-time"></i>15 min.</span><span class="cost"><i class="ico-euro">€</i>12,00</span></div>
      <div class="row"><span>Ablackieren</span><span class="dur"><i class="ico-time"></i>5 min.</span><span class="cost"><i class="ico-euro">€</i>4,00</span></div>
      <div class="row"><span>French</span><span class="dur"><i class="ico-time"></i>10 min.</span><span class="cost"><i class="ico-euro">€</i>5,00</span></div>
    </div>
    <h2 class="section-title abs" style="left:16px;top:190px;font-size:13px">Nageldesign</h2>
    <p class="intro abs" style="left:16px;top:208px;width:300px;font-size:6px">Gepflegte Hände sind täglich unsere Visitenkarte. Von der klassischen Maniküre bis hin zur Nagelmodellage finden Sie garantiert die passende Behandlung.</p>
    <div class="price-box is-small" style="left:16px;top:240px;width:300px">
      <span class="price-label">Nageldesign</span>
      <div class="row"><span>Maniküre</span><span class="dur"><i class="ico-time"></i>20 min.</span><span class="cost"><i class="ico-euro">€</i>17,00</span></div>
      <div class="row"><span>Dauerhafter Nagellack</span><span class="dur"><i class="ico-time"></i>45 min.</span><span class="cost"><i class="ico-euro">€</i>25,00</span></div>
      <div class="row"><span>Gelmodellage mit neu Verlängerung</span><span class="dur"><i class="ico-time"></i>90 min.</span><span class="cost"><i class="ico-euro">€</i>64,50</span></div>
      <div class="row"><span>Gelmodellage auffüllen</span><span class="dur"><i class="ico-time"></i>75 min.</span><span class="cost"><i class="ico-euro">€</i>46,50</span></div>
      <div class="row"><span>Naturnagelverstärkung</span><span class="dur"><i class="ico-time"></i>60 min.</span><span class="cost"><i class="ico-euro">€</i>39,50</span></div>
      <div class="row"><span>Fresh up</span><span class="dur"><i class="ico-time"></i>45 min.</span><span class="cost"><i class="ico-euro">€</i>20,00</span></div>
      <div class="row"><span>Wellnessmaniküre</span><span class="dur"><i class="ico-time"></i>35 min.</span><span class="cost"><i class="ico-euro">€</i>35,00</span></div>
    </div>
    <div class="photo" role="img" aria-label="Foto: Maniküre an einer Frauenhand mit Nagelfeile" style="left:0;top:500px;width:100%;height:207px;background:linear-gradient(135deg,#f3e6df,#e8d2c6 55%,#d9c0b3)"></div>
    <svg class="wave" style="top:480px;height:60px" viewBox="0 0 333 60" preserveAspectRatio="none" aria-hidden="true"><path d="M0,30 C70,60 150,10 220,28 C270,40 300,20 333,18 L333,0 L0,0 Z" fill="#fff"/><path d="M0,30 C70,60 150,10 220,28 C270,40 300,20 333,18" fill="none" stroke="#e874ab" stroke-width="5"/></svg>
  </div>

  <div class="panel panel-2">
    <div class="photo" role="img" aria-label="Foto: heller Empfangsbereich des Studios mit Holzboden" style="left:0;top:0;width:100%;height:190px;background:linear-gradient(160deg,#efe6d6,#d9c3a0 60%,#c7a877)"></div>
    <svg class="wave" style="top:150px;height:60px" viewBox="0 0 333 60" preserveAspectRatio="none" aria-hidden="true"><path d="M0,40 C80,10 150,60 240,30 C290,15 320,25 333,20 L333,60 L0,60 Z" fill="#fff"/></svg>
    <div class="photo" role="img" aria-label="Foto: das Team des Studios" style="left:190px;top:110px;width:120px;height:90px;border-radius:12px;border:3px solid var(--magenta);background:linear-gradient(135deg,#d7c8c2,#8e7d78)"></div>
    <div class="brand abs" style="left:0;top:226px;width:200px;font-size:18px"><span class="brand-dot"></span>lumara</div>
    <h3 class="section-title abs" style="left:26px;top:272px;font-size:11px">Öffnungszeiten</h3>
    <div class="hours abs" style="left:26px;top:292px;width:160px">
      <span>Mo, Di, Fr.</span><span>8:30 – 17:00 Uhr</span>
      <span>Mittwoch</span><span>8:30 – 18:00 Uhr</span>
      <span>Donnerstag</span><span>8:30 – 19:00 Uhr</span>
      <span style="grid-column:1/3">Samstag und Abendtermine nach Vereinbarung</span>
    </div>
    <div class="phone-card" style="left:200px;top:300px;width:106px;height:92px">
      <svg width="14" height="14" viewBox="0 0 24 24" aria-hidden="true"><path d="M6.6 10.8a15.5 15.5 0 0 0 6.6 6.6l2.2-2.2a1 1 0 0 1 1-.25 11.4 11.4 0 0 0 3.6.57 1 1 0 0 1 1 1V20a1 1 0 0 1-1 1A17 17 0 0 1 3 4a1 1 0 0 1 1-1h3.5a1 1 0 0 1 1 1c0 1.250.2 2.450.57 3.6a1 1 0 0 1-.25 1z" fill="#fff"/></svg>
      <span class="label" style="font-size:7px;margin-top:4px">TERMINE:</span>
      <span class="number" style="font-size:14px">0831 55<br>20 714</span>
    </div>
    <svg class="wave" style="top:395px;height:60px" viewBox="0 0 333 60" preserveAspectRatio="none" aria-hidden="true"><path d="M0,40 C70,20 140,50 220,25 C270,10 310,20 333,12 L333,60 L0,60 Z" fill="#5a5a5a"/><path d="M0,50 C70,28 140,58 220,35 C270,22 310,30 333,22 L333,60 L0,60 Z" fill="#e874ab"/></svg>
    <div class="pink-fill" style="top:454px;height:253px"></div>
    <div class="photo" role="img" aria-label="Foto: Behandlungsraum des Studios" style="left:150px;top:430px;width:60px;height:48px;border-radius:6px;border:2px solid #fff;background:linear-gradient(135deg,#f4ece2,#cdb898)"></div>
    <p class="abs" style="left:22px;top:485px;color:#fff;font-size:9px;font-weight:600;line-height:1.15">Wir freuen uns auf<br>Ihren Besuch</p>
    <p class="contact-title abs" style="left:22px;top:515px;font-size:7px">Kontakt</p>
    <div class="contact-line abs" style="left:22px;top:530px;font-size:6px"><svg width="6" height="8" viewBox="0 0 12 16" aria-hidden="true"><path d="M6 0a6 6 0 0 1 6 6c0 4.5-6 10-6 10S0 10.5 0 6a6 6 0 0 1 6-6zm0 3.5A2.5 2.5 0 1 0 6 8.5 2.5 2.5 0 0 0 6 3.5z" fill="#fff"/></svg><span>Lindenweg 14<br>87600 Kaufbeuren</span></div>
    <div class="contact-line abs" style="left:150px;top:530px;font-size:6px"><span>Telefon:&nbsp; 0831 55 20 714<br>E-Mail:&nbsp;&nbsp; info@lumara-studio.de</span></div>
    <div class="url-pill" style="left:90px;top:575px;width:155px;height:18px;font-size:9px;line-height:18px">www.lumara-studio.de</div>
  </div>

  <div class="panel panel-3">
    <div class="top-rule" style="height:4px"></div>
    <div class="brand abs" style="left:0;top:44px;width:100%;font-size:22px"><span class="brand-dot"></span>lumara</div>
    <div class="photo" role="img" aria-label="Foto: lächelnde Frau mit gepflegter Haut" style="left:0;top:95px;width:100%;height:430px;background:linear-gradient(160deg,#f4f1ef,#ead7cc 55%,#d9bcae)"></div>
    <svg class="wave" style="top:85px;height:50px" viewBox="0 0 333 50" preserveAspectRatio="none" aria-hidden="true"><path d="M0,30 C60,5 130,45 210,25 C270,10 310,15 333,10 L333,0 L0,0 Z" fill="#fff"/></svg>
    <div class="phone-card" style="left:205px;top:350px;width:106px;height:92px">
      <svg width="14" height="14" viewBox="0 0 24 24" aria-hidden="true"><path d="M6.6 10.8a15.5 15.5 0 0 0 6.6 6.6l2.2-2.2a1 1 0 0 1 1-.25 11.4 11.4 0 0 0 3.6.57 1 1 0 0 1 1 1V20a1 1 0 0 1-1 1A17 17 0 0 1 3 4a1 1 0 0 1 1-1h3.5a1 1 0 0 1 1 1c0 1.25.2 2.45.57 3.6a1 1 0 0 1-.25 1z" fill="#fff"/></svg>
      <span class="label" style="font-size:7px;margin-top:4px">TERMINE:</span>
      <span class="number" style="font-size:14px">0831 55<br>20 714</span>
    </div>
    <svg class="wave" style="top:430px;height:70px" viewBox="0 0 333 70" preserveAspectRatio="none" aria-hidden="true"><path d="M0,40 C80,15 150,55 230,30 C280,15 310,20 333,14 L333,70 L0,70 Z" fill="#5a5a5a"/><path d="M0,52 C80,26 150,64 230,40 C280,26 310,30 333,24 L333,70 L0,70 Z" fill="#e874ab"/></svg>
    <div class="pink-fill" style="top:498px;height:209px"></div>
    <div class="headline-white abs" style="left:0;top:545px;width:100%;font-size:30px">PREISLISTE</div>
    <div class="subline abs" style="left:0;top:584px;width:100%;font-size:10px">für 2019</div>
    <div class="url-pill" style="left:88px;top:620px;width:160px;height:18px;font-size:9px;line-height:18px">www.lumara-studio.de</div>
  </div>
</section>

<section class="sheet trifold trifold-inside" aria-label="Preisliste Innenseite">

  <div class="panel panel-1">
    <div class="top-rule" style="height:4px;width:70%"></div>
    <h2 class="section-title abs" style="left:16px;top:26px;font-size:13px">Wimpernverlängerung</h2>
    <p class="intro abs" style="left:16px;top:44px;width:300px;font-size:6px">Mit einer professionellen Wimpernverlängerung oder Wimpernverdichtung der Nova Beautyline gehört Wimperntusche der Vergangenheit an.</p>
    <div class="price-box is-small" style="left:16px;top:72px;width:300px">
      <span class="price-label">Wimpernverlängerung</span>
      <div class="row"><span>Neukunde</span><span class="dur"><i class="ico-time"></i>150 min.</span><span class="cost"><i class="ico-euro">€</i>190,00</span></div>
      <div class="row"><span>Neukunde Volumentechnik</span><span class="dur"><i class="ico-time"></i>180 min.</span><span class="cost"><i class="ico-euro">€</i>280,00</span></div>
      <div class="row"><span>Refill nach 2 Wochen</span><span class="dur"><i class="ico-time"></i>45 min.</span><span class="cost"><i class="ico-euro">€</i>45,00</span></div>
      <div class="row"><span>Refill nach 3 Wochen</span><span class="dur"><i class="ico-time"></i>60 min.</span><span class="cost"><i class="ico-euro">€</i>52,00</span></div>
      <div class="row"><span>Refill nach 4 Wochen</span><span class="dur"><i class="ico-time"></i>90 min.</span><span class="cost"><i class="ico-euro">€</i>65,00</span></div>
      <div class="row"><span>Wimpernverlängerung entfernen</span><span class="dur"><i class="ico-time"></i>30 min.</span><span class="cost"><i class="ico-euro">€</i>20,00</span></div>
      <div class="row"><span>Volumentechnik Zuschlag</span><span class="dur"><i class="ico-time"></i>30 min.</span><span class="cost"><i class="ico-euro">€</i>15,00</span></div>
    </div>
    <h2 class="section-title abs" style="left:16px;top:180px;font-size:13px">Wimpernlifting</h2>
    <p class="intro abs" style="left:16px;top:198px;width:300px;font-size:6px">Mit einem professionellen Wimpernlifting erhalten Ihre eigenen Wimpern einen natürlichen, offenen Schwung für bis zu acht Wochen.</p>
    <div class="price-box is-small" style="left:16px;top:228px;width:300px">
      <span class="price-label">Wimpernlifting</span>
      <div class="row"><span>Neukunde</span><span class="dur"><i class="ico-time"></i>90 min.</span><span class="cost"><i class="ico-euro">€</i>190,00</span></div>
      <div class="row"><span>Neukunde Volumentechnik</span><span class="dur"><i class="ico-time"></i>90 min.</span><span class="cost"><i class="ico-euro">€</i>280,00</span></div>
      <div class="row"><span>Refill nach 2 Wochen</span><span class="dur"><i class="ico-time"></i>45 min.</span><span class="cost"><i class="ico-euro">€</i>45,00</span></div>
    </div>
    <div class="photo" role="img" aria-label="Foto: Frauenaugen mit langen Wimpern" style="left:0;top:300px;width:100%;height:407px;background:linear-gradient(160deg,#f3eeeb,#e2d3cb 60%,#c9d6e2)"></div>
    <svg class="wave" style="top:290px;height:70px" viewBox="0 0 333 70" preserveAspectRatio="none" aria-hidden="true"><path d="M0,20 L333,20 L333,40 C260,65 190,20 110,45 C60,60 20,40 0,45 Z" fill="#fff"/><path d="M333,40 C260,65 190,20 110,45 C60,60 20,40 0,45" fill="none" stroke="#e874ab" stroke-width="5"/><rect x="0" y="0" width="333" height="21" fill="#fff"/></svg>
  </div>

  <div class="panel panel-2">
    <div class="photo" role="img" aria-label="Foto: Behandlungsraum mit Kosmetikliege" style="left:0;top:0;width:100%;height:215px;background:linear-gradient(160deg,#f5f1ec,#ddd1c4 55%,#b39f8b)"></div>
    <svg class="wave" style="top:170px;height:60px" viewBox="0 0 333 60" preserveAspectRatio="none" aria-hidden="true"><path d="M0,25 C70,5 140,40 220,30 C280,22 310,35 333,30 L333,60 L0,60 Z" fill="#fff"/><path d="M0,25 C70,5 140,40 220,30 C280,22 310,35 333,30" fill="none" stroke="#e874ab" stroke-width="5"/></svg>
    <h2 class="section-title abs" style="left:0;top:228px;width:100%;text-align:center;font-size:13px">Kosmetikbehandlungen</h2>
    <div class="pill-sub" style="left:80px;top:248px;width:175px">Fresh Start - Encore Konzept</div>
    <div class="body-copy abs" style="left:26px;top:270px;width:282px;text-align:center">
      <p>Beim ersten Besuch analysieren wir Ihre Haut in Ruhe und stellen eine Pflege zusammen, die genau zu Ihnen passt. Reinigung, Peeling und Maske bereiten die Haut optimal vor.</p>
      <p style="margin-top:6px">Bei jedem weiteren Termin bauen wir auf diesem Fundament auf. So wird Ihre Behandlung Schritt für Schritt feiner abgestimmt und die Ergebnisse bleiben sichtbar länger erhalten. Wirkstoffe und Massage wählen wir individuell aus.</p>
      <p style="margin-top:6px">Zum Abschluss erhalten Sie eine persönliche Empfehlung für die Pflege zu Hause, damit Ihre Haut auch zwischen den Terminen strahlt.</p>
    </div>
    <div class="price-box is-small" style="left:26px;top:420px;width:282px">
      <span class="price-label">Fresh Start - Encore</span>
      <div class="row"><span>Fresh Start Analyse</span><span class="dur"><i class="ico-time"></i>90 min.</span><span class="cost"><i class="ico-euro">€</i>190,00</span></div>
      <div class="row"><span>Encore Intensiv</span><span class="dur"><i class="ico-time"></i>90 min.</span><span class="cost"><i class="ico-euro">€</i>280,00</span></div>
      <div class="row"><span>Encore Kompakt</span><span class="dur"><i class="ico-time"></i>45 min.</span><span class="cost"><i class="ico-euro">€</i>45,00</span></div>
    </div>
    <p class="body-copy abs" style="left:26px;top:476px;width:282px;text-align:center">Alle Behandlungen sind mit weiteren Bausteinen kombinierbar. Wir beraten Sie gerne persönlich.</p>
  </div>

  <div class="panel panel-3">
    <div class="top-rule" style="height:4px;width:50%;left:50%"></div>
    <h2 class="section-title abs" style="left:16px;top:26px;font-size:12px">Enthaarung mit Zuckerpaste</h2>
    <p class="intro abs" style="left:16px;top:44px;width:300px;font-size:6px">Sanft, natürlich und hautfreundlich: Die Zuckerpaste entfernt Haare samt Wurzel und hinterlässt glatte Haut für mehrere Wochen.</p>
    <div class="price-box is-small" style="left:16px;top:78px;width:300px">
      <span class="price-label">Enthaarung</span>
      <div class="row"><span>Beratungsgespräch Sugaring + Gesicht</span><span class="dur"><i class="ico-time"></i>20 min.</span><span class="cost"><i class="ico-euro">€</i>20,00</span></div>
      <div class="row"><span>Unterschenkel inkl. Knie</span><span class="dur"><i class="ico-time"></i>30 min.</span><span class="cost"><i class="ico-euro">€</i>45,00</span></div>
      <div class="row"><span>Beine komplett</span><span class="dur"><i class="ico-time"></i>60 min.</span><span class="cost"><i class="ico-euro">€</i>75,00</span></div>
      <div class="row"><span>Arme komplett</span><span class="dur"><i class="ico-time"></i>30 min.</span><span class="cost"><i class="ico-euro">€</i>40,00</span></div>
      <div class="row"><span>Achseln</span><span class="dur"><i class="ico-time"></i>15 min.</span><span class="cost"><i class="ico-euro">€</i>20,00</span></div>
      <div class="row"><span>Teile Gesicht</span><span class="dur"><i class="ico-time"></i>10 min.</span><span class="cost"><i class="ico-euro">€</i>12,00</span></div>
      <div class="row"><span>Bikinizone</span><span class="dur"><i class="ico-time"></i>20 min.</span><span class="cost"><i class="ico-euro">€</i>32,00</span></div>
      <div class="row"><span>Nasen- und Ohrenhaare</span><span class="dur"><i class="ico-time"></i>10 min.</span><span class="cost"><i class="ico-euro">€</i>10,00</span></div>
      <div class="row"><span>Rücken</span><span class="dur"><i class="ico-time"></i>30 min.</span><span class="cost"><i class="ico-euro">€</i>54,00</span></div>
      <div class="row"><span>Intim (nur für Damen)</span><span class="dur"><i class="ico-time"></i>45 min.</span><span class="cost"><i class="ico-euro">€</i>68,00</span></div>
      <div class="row"><span>Bauch</span><span class="dur"><i class="ico-time"></i>20 min.</span><span class="cost"><i class="ico-euro">€</i>32,00</span></div>
      <div class="row"><span>Brust</span><span class="dur"><i class="ico-time"></i>20 min.</span><span class="cost"><i class="ico-euro">€</i>32,00</span></div>
      <div class="row"><span>Oberlippe</span><span class="dur"><i class="ico-time"></i>10 min.</span><span class="cost"><i class="ico-euro">€</i>10,00</span></div>
    </div>
    <div class="photo" role="img" aria-label="Foto: Enthaarung am Bein mit Zuckerpaste" style="left:0;top:290px;width:100%;height:417px;background:linear-gradient(160deg,#efe2d6,#d9b79e 50%,#8c7a66)"></div>
    <svg class="wave" style="top:280px;height:70px" viewBox="0 0 333 70" preserveAspectRatio="none" aria-hidden="true"><rect x="0" y="0" width="333" height="21" fill="#fff"/><path d="M0,20 L333,20 L333,35 C280,60 200,15 120,40 C70,55 30,35 0,42 Z" fill="#fff"/><path d="M333,35 C280,60 200,15 120,40 C70,55 30,35 0,42" fill="none" stroke="#e874ab" stroke-width="5"/></svg>
  </div>
</section>

<section class="sheet flyer flyer-front" aria-label="Angebote für Männer – Titelseite">
  <div class="top-rule"></div>
  <div class="brand abs" style="left:0;top:78px;width:100%;font-size:34px"><span class="brand-dot"></span>lumara</div>
  <div class="photo" role="img" aria-label="Foto: gepflegter Mann mit Bart, Hand am Kinn" style="left:0;top:150px;width:100%;height:480px;background:linear-gradient(160deg,#e9e9eb,#d9cbc2 50%,#b39a8a)"></div>
  <svg class="wave" style="top:130px;height:60px" viewBox="0 0 398 60" preserveAspectRatio="none" aria-hidden="true"><path d="M0,0 L398,0 L398,28 C330,30 290,-5 220,12 C150,30 80,45 0,48 Z" fill="#fff"/><path d="M0,48 C80,45 150,30 220,12 C290,-5 330,30 398,28" fill="none" stroke="#5a5a5a" stroke-width="6"/></svg>
  <svg class="wave" style="top:560px;height:80px" viewBox="0 0 398 80" preserveAspectRatio="none" aria-hidden="true"><path d="M0,35 C90,60 180,25 270,40 C330,50 370,35 398,30 L398,80 L0,80 Z" fill="#5a5a5a"/><path d="M0,45 C90,70 180,35 270,50 C330,60 370,45 398,40 L398,80 L0,80 Z" fill="#e874ab"/></svg>
  <div class="pink-fill" style="top:638px;height:159px"></div>
  <div class="phone-card" style="left:233px;top:490px;width:132px;height:136px">
    <svg width="22" height="22" viewBox="0 0 24 24" aria-hidden="true"><path d="M6.6 10.8a15.5 15.5 0 0 0 6.6 6.6l2.2-2.2a1 1 0 0 1 1-.25 11.4 11.4 0 0 0 3.6.57 1 1 0 0 1 1 1V20a1 1 0 0 1-1 1A17 17 0 0 1 3 4a1 1 0 0 1 1-1h3.5a1 1 0 0 1 1 1c0 1.25.2 2.45.57 3.6a1 1 0 0 1-.25 1z" fill="#fff"/></svg>
    <span class="label" style="font-size:13px;margin-top:10px">TERMINE:</span>
    <span class="number" style="font-size:22px;margin-top:4px">0831 55<br>20 714</span>
  </div>
  <div class="headline-white abs" style="left:0;top:655px;width:100%;font-size:44px">ANGEBOTE</div>
  <div class="subline abs" style="left:0;top:710px;width:100%;font-size:15px">für Männer</div>
  <div class="url-pill" style="left:87px;top:745px;width:204px;height:26px;font-size:15px;line-height:26px">www.lumara-studio.de</div>
</section>

<section class="sheet flyer flyer-back" aria-label="Angebote für Männer – Preise">
  <div class="top-rule"></div>
  <h1 class="section-title abs" style="left:33px;top:32px;font-size:19px">Angebote für Männer</h1>
  <div class="abs" style="left:0;top:66px;width:370px;height:1px;background:#999"></div>
  <p class="intro abs" style="left:33px;top:80px;width:340px;font-size:9px">Mit einer professionellen Wimpernverlängerung oder Wimpernverdichtung der Nova Beautyline gehört Wimperntusche der Vergangenheit an.</p>

  <div class="price-box is-large" style="left:34px;top:130px;width:331px">
    <span class="price-label">Kosmetikbehandlungen</span>
    <div class="row"><span>Lorem ipsum dolor</span><span class="dur"><i class="ico-time"></i>90 min.</span><span class="cost"><i class="ico-euro">€</i>190,00</span></div>
    <div class="row"><span>Lorem ipsum dolor</span><span class="dur"><i class="ico-time"></i>90 min.</span><span class="cost"><i class="ico-euro">€</i>280,00</span></div>
    <div class="row"><span>Lorem ipsum dolor</span><span class="dur"><i class="ico-time"></i>45 min.</span><span class="cost"><i class="ico-euro">€</i>45,00</span></div>
    <div class="row"><span>Lorem ipsum dolor</span><span class="dur"><i class="ico-time"></i>60 min.</span><span class="cost"><i class="ico-euro">€</i>52,00</span></div>
  </div>

  <div class="price-box is-large" style="left:34px;top:254px;width:331px">
    <span class="price-label">Massagen</span>
    <div class="row"><span>Lorem ipsum dolor</span><span class="dur"><i class="ico-time"></i>90 min.</span><span class="cost"><i class="ico-euro">€</i>190,00</span></div>
    <div class="row"><span>Lorem ipsum dolor</span><span class="dur"><i class="ico-time"></i>90 min.</span><span class="cost"><i class="ico-euro">€</i>280,00</span></div>
    <div class="row"><span>Lorem ipsum dolor</span><span class="dur"><i class="ico-time"></i>45 min.</span><span class="cost"><i class="ico-euro">€</i>45,00</span></div>
    <div class="row"><span>Lorem ipsum dolor</span><span class="dur"><i class="ico-time"></i>60 min.</span><span class="cost"><i class="ico-euro">€</i>52,00</span></div>
  </div>

  <div class="price-box is-large" style="left:34px;top:377px;width:331px">
    <span class="price-label">Maniküre</span>
    <div class="row"><span>Lorem ipsum dolor</span><span class="dur"><i class="ico-time"></i>90 min.</span><span class="cost"><i class="ico-euro">€</i>190,00</span></div>
    <div class="row"><span>Lorem ipsum dolor</span><span class="dur"><i class="ico-time"></i>90 min.</span><span class="cost"><i class="ico-euro">€</i>280,00</span></div>
  </div>

  <div class="price-box is-large" style="left:34px;top:461px;width:331px">
    <span class="price-label">Fußpflege</span>
    <div class="row"><span>Lorem ipsum dolor</span><span class="dur"><i class="ico-time"></i>90 min.</span><span class="cost"><i class="ico-euro">€</i>190,00</span></div>
    <div class="row"><span>Lorem ipsum dolor</span><span class="dur"><i class="ico-time"></i>90 min.</span><span class="cost"><i class="ico-euro">€</i>280,00</span></div>
    <div class="row"><span>Lorem ipsum dolor</span><span class="dur"><i class="ico-time"></i>45 min.</span><span class="cost"><i class="ico-euro">€</i>45,00</span></div>
    <div class="row"><span>Lorem ipsum dolor</span><span class="dur"><i class="ico-time"></i>60 min.</span><span class="cost"><i class="ico-euro">€</i>52,00</span></div>
    <div class="row"><span>Lorem ipsum dolor</span><span class="dur"><i class="ico-time"></i>45 min.</span><span class="cost"><i class="ico-euro">€</i>45,00</span></div>
  </div>

  <svg class="wave" style="top:595px;height:80px" viewBox="0 0 398 80" preserveAspectRatio="none" aria-hidden="true"><path d="M0,58 C60,60 110,50 160,30 C200,12 230,15 270,35 C320,55 360,55 398,52 L398,80 L0,80 Z" fill="#5a5a5a"/><path d="M0,62 C70,64 130,50 180,40 C220,32 260,45 300,55 C340,62 370,58 398,56 L398,80 L0,80 Z" fill="#e874ab"/></svg>
  <div class="pink-fill" style="top:673px;height:124px"></div>
  <p class="contact-title abs" style="left:20px;top:680px;font-size:11px">Kontakt</p>
  <div class="contact-line abs" style="left:20px;top:704px;font-size:10px"><svg width="9" height="12" viewBox="0 0 12 16" aria-hidden="true"><path d="M6 0a6 6 0 0 1 6 6c0 4.5-6 10-6 10S0 10.5 0 6a6 6 0 0 1 6-6zm0 3.5A2.5 2.5 0 1 0 6 8.5 2.5 2.5 0 0 0 6 3.5z" fill="#fff"/></svg><span>Lindenweg 14<br>87600 Kaufbeuren</span></div>
  <div class="contact-line abs" style="left:172px;top:704px;font-size:10px">
    <svg width="10" height="10" viewBox="0 0 24 24" aria-hidden="true"><path d="M6.6 10.8a15.5 15.5 0 0 0 6.6 6.6l2.2-2.2a1 1 0 0 1 1-.25 11.4 11.4 0 0 0 3.6.57 1 1 0 0 1 1 1V20a1 1 0 0 1-1 1A17 17 0 0 1 3 4a1 1 0 0 1 1-1h3.5a1 1 0 0 1 1 1c0 1.25.2 2.45.57 3.6a1 1 0 0 1-.25 1z" fill="#fff"/></svg>
    <span>Telefon:&nbsp;&nbsp; 0831 55 20 714<br>E-Mail:&nbsp;&nbsp;&nbsp; info@lumara-studio.de</span>
  </div>
  <div class="url-pill" style="left:92px;top:750px;width:214px;height:27px;font-size:16px;line-height:27px">www.lumara-studio.de</div>
</section>

</body>
</html>
```